We need a professional contract designs with our logo

We need a contract designed on a form with our logo etc to make it look more professional and not just a word document

Also we need a cover for the contract too.

Industry/Entity Type

It Professional

```html
<!DOCTYPE html>
<html lang="en">
<head>
<meta charset="utf-8">
<title>Room Tenancy Agreement – Page 5</title>
<link href="https://fonts.googleapis.com/css2?family=Lato:wght@400;700&display=swap" rel="stylesheet">
<style>
  :root {
    --page-bg: #712d71;
    --ink: #ffffff;
    --rule: rgba(255, 255, 255, 0.55);
  }
  html, body {
    margin: 0;
    padding: 0;
    width: 849px;
    height: 1200px;
    overflow: hidden;
    background: var(--page-bg);
  }
  .page {
    position: relative;
    width: 849px;
    height: 1200px;
    background: var(--page-bg);
    color: var(--ink);
    font-family: "Lato", "Gill Sans", sans-serif;
    font-size: 10px;
    line-height: 11.65px;
    letter-spacing: -0.05px;
  }
  .column {
    position: absolute;
    top: 39px;
    white-space: nowrap;
  }
  .column--left { left: 55px; }
  .column--right { left: 467px; }
  .carry-over { padding-left: 37px; }
  .section-title { font-weight: 700; margin: 0; font-size: 10px; line-height: 11.65px; }
  .clause { padding-left: 15px; text-indent: -4px; }
  .column--right .clause { padding-left: 14px; text-indent: -14px; }
  .column--right .subclause { padding-left: 38px; text-indent: -24px; }
  .footer-rule {
    position: absolute;
    left: 40px;
    top: 547px;
    width: 768px;
    height: 1px;
    background: var(--rule);
  }
  .copyright {
    position: absolute;
    left: 40px;
    top: 558px;
    font-size: 7px;
    line-height: 9px;
    white-space: nowrap;
  }
  .page-number {
    position: absolute;
    right: 41px;
    top: 1171px;
    font-size: 13.5px;
    line-height: 16px;
    white-space: nowrap;
  }
  .page-number strong { font-weight: 700; }
  .page-number .divider { padding: 0 5px; }
</style>
</head>
<body>
<main class="page">
  <section class="column column--left">
    <div class="carry-over">
      come to an end, subject to the Landlord complying with the proper<br>
      legal procedure. The Landlord retains all his other rights in respect<br>
      of the Tenant’s obligations under this Agreement. Note that if<br>
      possession of the Property has not been surrendered and anyone<br>
      is living at the Property or if the tenancy is an assured or assured<br>
      shorthold tenancy then the landlord must obtain a court order for<br>
      possession before re-entering the Property. This clause does not<br>
      affect the Tenant’s rights under the Protection from Eviction Act<br>
      1977.
    </div>
    <h2 class="section-title">5. The Deposit</h2>
    <div class="clause">5.1 The Deposit will be held in accordance with the Tenancy Deposit<br>Scheme Rules as issued by the relevant Tenancy Deposit Scheme.</div>
    <div class="clause">5.2. No interest will be payable to the Tenant by the Landlord in respect of<br>the Deposit.</div>
    <div class="clause">5.3. Subject to any relevant provisions of the Tenancy Deposit Scheme Rules,<br>
      the Landlord shall be entitled to claim from the Deposit the reasonable<br>
      cost of any repairs or damage to the Property or its contents caused by<br>
      the Tenant (including any damage caused by the Tenant’s family and<br>
      visitors) and for any other financial losses suffered by the Landlord as a<br>
      result of the Tenant’s breach of these terms and conditions, provided<br>
      the sum claimed by the Landlord is reasonably incurred and is<br>
      reasonable in amount. The Landlord is not entitled to claim in respect<br>
      of any damage to the Property or its contents which is due to ‘fair<br>
      wear and tear’ i.e. which is as a result of the Tenant and his family (if<br>
      any) living in the property and using it in a reasonable and lawful manner.</div>
    <h2 class="section-title">6. Other provisions</h2>
    <div class="clause">6.1 The Landlord hereby notifies the Tenant under Section 48 of the<br>
      Landlord &amp; Tenant Act 1987 that any notices (including notices in<br>
      proceedings) should be served upon the Landlord at the address stated<br>
      with the name of the Landlord overleaf.</div>
    <div class="clause">6.2 The Landlord shall be entitled to have and retain keys for all the doors<br>
      to the Property but shall not be entitled to use these to enter the<br>
      Designated Room without the consent of the Tenant (save in an<br>
      emergency).</div>
    <div class="clause">6.3 Any notices or other documents shall be deemed served on the Tenant<br>
      during the tenancy by either being left at the Property or by being sent<br>
      to the Tenant at the Property by first-class post. If notices or other<br>
      documents are served on the Tenant by post they shall be deemed<br>
      served on the day after posting.</div>
    <div class="clause">6.4 Any person other than the Tenant who pays the rent due hereunder or<br>
      any part thereof to the Landlord shall be deemed to have made such<br>
      payment as agent for and on behalf of the Tenant which the Landlord<br>
      shall be entitled to assume without enquiry.</div>
  </section>

  <section class="column column--right">
    <div class="clause">6.5 Any personal items left behind at the end of the tenancy after the<br>
      Tenant has vacated (which the Tenant has not removed in accordance<br>
      with clause 2.13 above) shall be considered abandoned if they have not<br>
      been removed within 14 days of written notice to the Tenant from the<br>
      Landlord, or if the Landlord has been unable to trace the Tenant by<br>
      taking reasonable steps to do so. After this period the Landlord may<br>
      remove or dispose of the items as he thinks fit. The Tenant shall be<br>
      liable for the reasonable disposal costs which may be deducted from<br>
      the proceeds of sale (if any), and the Tenant shall remain liable for any<br>
      balance. Any net proceeds of the sale to be returned to the Tenant at<br>
      the forwarding address provided to the Landlord.</div>
    <div class="clause">6.6 In the event of damage to or destruction of the Property by any of the<br>
      risks insured against by the Landlord the Tenant shall be relieved from<br>
      payment of the Rent to the extent that the Tenant’s use and enjoyment<br>
      of the Property is thereby prevented and from performance of its<br>
      obligations as to the state and condition of the Property to the extent of<br>
      and so long as there prevails such damage or destruction (except to the<br>
      extent that the insurance is prejudiced by any act or default of the<br>
      Tenant).</div>
    <div class="clause">6.7 Where the context so admits:</div>
    <div class="subclause">6.7.1 The ‘Landlord’ includes the persons from time to time entitled to<br>receive the Rent.</div>
    <div class="subclause">6.7.2 The ‘Tenant’ includes any persons deriving title under the Tenant.</div>
    <div class="subclause">6.7.3 The ‘Designated Room’ and ‘Shared Parts’ includes any part or<br>
      parts of the Designated Room and Shared Parts and all of the<br>
      Landlord’s fixtures and fittings in the Designated Room and Shared<br>
      Parts.</div>
    <div class="subclause">6.7.4 All references to the singular shall include the plural and vice versa<br>
      and any obligations or liabilities of more than one person shall be<br>
      joint and several (this means that they will each be liable for all<br>
      sums due under this Agreement, not just liable for a proportionate<br>
      part) and an obligation on the part of a party shall include an<br>
      obligation not to allow or permit the breach of that obligation.<br>
      Note that joint and several liability will only apply to two or more<br>
      Tenants signing this Agreement together. Tenants will not have<br>
      joint and several liability with other tenants in the Property who<br>
      have signed separate agreements with the Landlord.</div>
    <div class="subclause">6.7.5 All references to ‘he’, ‘him’ and ‘his’ shall be taken to include ‘she’,<br>‘her’ and ‘hers’.</div>
    <div class="subclause">6.7.6 Any clause requiring the Tenant to do or not do something in<br>
      relation to the Property should be read as requiring the Tenant to<br>
      do or not do the same thing in relation to the Designated Room.</div>
  </section>

  <div class="footer-rule"></div>
  <p class="copyright" style="margin:0">© 2014 Corvell Rooms Publishing Limited. This agreement may not be photocopied or reproduced in any form.</p>

  <p class="page-number" style="margin:0"><strong>5</strong><span class="divider">|</span>Page</p>
</main>
</body>
</html>
```